Flyer: Steady Steps, Bright Days

Please create a two (2) page flyer. We welcome minor updates/ changes to the Steady Steps Bright Days flyer that is attached as a word document. We are aiming for the same general look and feel as the original PDF attached (please note that we have updated the content and would like the designers to use what is listed in the word document).
We encourage you to provide multiple versions using pictures of different people we have on hand. Our team currently likes how the lady in the picture is looking in the direction of the text - we encourage designers to please flip the photo if needed to make this possible. We also give the permission to crop the photos as needed to fit the design better aesthetically. In addition, the team wondered about having a pdf file that allows the user to easily change out the graphic between different photos to reflect different communities best—not sure if that is as easy as it sounds. Please remember to include the funding statement - you can find it within both of the current documents. For more information about our project, please visit https://novelmarrow.org/wellness-path/

```html
<!DOCTYPE html>
<html lang="en">
<head>
<meta charset="utf-8">
<title>Steady Steps, Bright Days – Flyer</title>
<link href="https://fonts.googleapis.com/css2?family=Montserrat:wght@500;600;700;800&family=Roboto:wght@400;500;700&display=swap" rel="stylesheet">
<style>
:root{
  --teal:#3c9fa9;
  --teal-dark:#2f8891;
  --red:#b04b45;
  --cyan-light:#bfe5e9;
  --ink:#3a3a3a;
  --white:#ffffff;
  --backdrop:#ececec;
}
*{box-sizing:border-box;margin:0;padding:0}
html,body{width:1200px;height:2400px;overflow:hidden;background:var(--backdrop)}
body{font-family:"Roboto",Arial,sans-serif;color:var(--ink);position:relative}
.page{position:absolute;left:193px;width:814px;height:1150px;background:var(--white);overflow:hidden;box-shadow:0 4px 18px rgba(0,0,0,.18)}
.page--front{top:30px}
.page--back{top:1220px}
.abs{position:absolute}
.heading{font-family:"Montserrat",Arial,sans-serif;font-weight:600;text-transform:uppercase;color:var(--teal);line-height:1.15}
.body-copy{font-size:13px;line-height:1.3;text-align:justify;color:var(--ink)}
.accent{color:var(--red);font-weight:500}

/* logo */
.brand{left:41px;top:48px;display:flex;align-items:center;gap:10px}
.brand__mark{width:26px;height:26px;background:var(--teal)}
.brand__name{font-family:"Montserrat",Arial,sans-serif;font-weight:700;font-size:20px;color:var(--teal);text-transform:uppercase;letter-spacing:.5px}

/* photo */
.photo{left:300px;top:0;width:514px;height:560px;background:linear-gradient(90deg,rgba(255,255,255,1) 0%,rgba(214,228,238,.7) 30%,#b7cfe0 55%,#a98a72 80%,#6e5244 100%)}

/* title */
.title{left:38px;top:160px;font-family:"Montserrat",Arial,sans-serif;font-weight:800;text-transform:uppercase;line-height:.95}
.title span{display:block}
.title__teal{color:var(--teal);font-size:64px;font-weight:700}
.title__red{color:var(--red);font-size:108px;letter-spacing:-2px}

/* stats */
.stats{left:451px;top:417px;width:325px;height:303px;background:var(--teal);border-radius:10px 10px 0 0;color:var(--white);padding:16px 22px}
.stat{display:flex;flex-direction:column;margin-bottom:14px}
.stat__row{display:flex;align-items:center;gap:14px}
.stat__icon{width:72px;height:52px}
.stat__num{font-family:"Montserrat",Arial,sans-serif;font-weight:600;font-size:56px;line-height:1}
.stat__text{font-size:17px;line-height:1.3;margin-left:28px}

/* keep section */
.keep{left:41px;top:581px;width:370px}
.keep .heading{font-size:18px;margin-bottom:8px}

/* risk band */
.risk{left:0;top:723px;width:814px;height:89px;background:var(--red)}
.risk__label{position:absolute;left:0;top:0;width:335px;height:89px;background:var(--teal);border-radius:0 45px 45px 0;padding:12px 0 0 41px;font-family:"Montserrat",Arial,sans-serif;font-weight:600;font-size:17px;line-height:1.2;color:#0f2f33;text-transform:uppercase}
.risk__item{position:absolute;top:18px;display:flex;align-items:center;gap:10px;color:var(--white);font-weight:700;font-size:16px;line-height:1.2}
.risk__item svg{width:48px;height:48px}

/* protect */
.protect-heading{left:38px;top:835px;font-size:19px}
.col{position:absolute;width:255px}
.tick-list{list-style:none}
.tick-list li{display:flex;gap:8px;font-size:12.5px;line-height:1.3;margin-bottom:18px}
.tick-list li svg{flex:0 0 12px;width:12px;height:12px;margin-top:2px}

/* footer */
.footer{left:0;bottom:0;width:814px;height:82px;background:var(--teal);display:flex;align-items:center;color:var(--white);padding-left:40px}
.footer__phone{display:flex;align-items:center;gap:14px;font-family:"Montserrat",Arial,sans-serif;font-weight:500;font-size:27px;width:300px}
.footer__addr{display:flex;align-items:center;gap:14px;font-size:13px;line-height:1.3;width:260px;border-right:1px solid rgba(255,255,255,.5);padding-right:10px}
.footer__web{display:flex;align-items:center;gap:14px;font-size:13px;padding-left:20px}
.footer svg{fill:var(--white)}

/* back page */
.river{left:0;top:0;width:814px;height:330px;background:var(--cyan-light)}
.river__copy{left:38px;top:38px;width:365px}
.river__kicker{font-size:20px;color:#1e1e1e}
.river__title{font-size:28px;color:var(--red);font-weight:600}
.river__copy .body-copy{margin-top:10px;font-size:12.5px}
.panel{left:435px;top:342px;width:379px;height:466px;background:var(--red);padding:40px 30px 0 30px;color:var(--white)}
.panel .tick-list li{margin-bottom:24px;font-size:12.5px}
.panel .tick-list li strong{font-weight:700}
.doctor-heading{left:38px;top:355px;font-size:23px}
.doctor{left:38px;top:408px;width:370px}
.doctor .tick-list li{margin-bottom:24px}
.steps-heading{left:35px;top:835px;font-size:23px}
</style>
</head>
<body>

<svg width="0" height="0" style="position:absolute">
  <defs>
    <symbol id="tick" viewBox="0 0 12 12"><circle cx="6" cy="6" r="5.2" fill="none" stroke="currentColor" stroke-width="1"/><path d="M3.5 6.2l1.8 1.8 3.4-3.6" fill="none" stroke="currentColor" stroke-width="1.1"/></symbol>
    <symbol id="phone" viewBox="0 0 24 24"><path d="M6.6 10.8a15.1 15.1 0 0 0 6.6 6.6l2.2-2.2a1 1 0 0 1 1-.25 11.4 11.4 0 0 0 3.6.57 1 1 0 0 1 1 1V20a1 1 0 0 1-1 1A17 17 0 0 1 3 4a1 1 0 0 1 1-1h3.5a1 1 0 0 1 1 1c0 1.25.2 2.45.57 3.57a1 1 0 0 1-.25 1z"/></symbol>
    <symbol id="pin" viewBox="0 0 24 24"><path d="M12 2a7 7 0 0 0-7 7c0 5.2 7 13 7 13s7-7.8 7-13a7 7 0 0 0-7-7zm0 9.5A2.5 2.5 0 1 1 12 6.5a2.5 2.5 0 0 1 0 5z"/></symbol>
    <symbol id="globe" viewBox="0 0 24 24"><path d="M12 2a10 10 0 1 0 0 20 10 10 0 0 0 0-20zm6.9 6h-2.9a15.7 15.7 0 0 0-1.4-3.6A8 8 0 0 1 18.9 8zM12 4c.8 1.2 1.5 2.5 1.9 4h-3.8c.4-1.5 1.1-2.8 1.9-4zM4.3 14a8.2 8.2 0 0 1 0-4h3.4a16 16 0 0 0 0 4zm.8 2h2.9c.3 1.3.8 2.5 1.4 3.6A8 8 0 0 1 5.1 16zM8 8H5.1a8 8 0 0 1 4.3-3.6C8.8 5.5 8.3 6.7 8 8zm4 12c-.8-1.2-1.5-2.5-1.9-4h3.8c-.4 1.5-1.1 2.8-1.9 4zm2.3-6H9.7a14.7 14.7 0 0 1 0-4h4.6a14.7 14.7 0 0 1 0 4zm.3 5.6c.6-1.1 1.1-2.3 1.4-3.6h2.9a8 8 0 0 1-4.3 3.6zm1.7-5.6a16 16 0 0 0 0-4h3.4a8.2 8.2 0 0 1 0 4z"/></symbol>
  </defs>
</svg>

<!-- FRONT PAGE -->
<section class="page page--front">
  <div class="abs photo" role="img" aria-label="Photo of a smiling older woman outdoors, looking toward the title, with sky and hills behind her"></div>

  <svg class="abs" style="left:0;top:0" width="814" height="1150" viewBox="0 0 814 1150" aria-hidden="true">
    <path d="M0 0 H440 C390 70 300 135 140 150 C80 155 30 150 0 152 Z" fill="#ffffff"/>
    <path d="M0 152 C30 150 80 155 140 150 C300 135 390 70 440 0" fill="none" stroke="#3c9fa9" stroke-width="6"/>
    <path d="M0 560 L0 590 C120 545 300 532 470 530 L814 525 L814 560 Z" fill="#ffffff"/>
    <path d="M0 597 C110 548 300 535 470 532" fill="none" stroke="#3c9fa9" stroke-width="7"/>
    <rect x="0" y="590" width="814" height="560" fill="#ffffff"/>
  </svg>

  <div class="abs brand"><span class="brand__mark"></span><span class="brand__name">Novel Marrow Alliance</span></div>

  <h1 class="abs title">
    <span class="title__teal">Steady</span>
    <span class="title__red">Steps</span>
    <span class="title__teal">Bright</span>
    <span class="title__red">Days</span>
  </h1>

  <div class="abs stats">
    <div class="stat">
      <div class="stat__row">
        <svg class="stat__icon" viewBox="0 0 72 52" fill="none" stroke="#e96a5e" stroke-width="2"><circle cx="16" cy="14" r="6"/><circle cx="36" cy="10" r="6"/><circle cx="56" cy="14" r="6"/><path d="M8 46V28h16v18M28 46V24h16v22M48 46V28h16v18"/></svg>
        <span class="stat__num">1 in9</span>
      </div>
      <p class="stat__text" style="margin-left:28px">People in the U.S. ages 65+<br>have Alzheimer’s dementia</p>
    </div>
    <div class="stat">
      <div class="stat__row">
        <svg class="stat__icon" viewBox="0 0 72 52" fill="none" stroke="#e96a5e" stroke-width="2"><circle cx="26" cy="12" r="7"/><circle cx="46" cy="16" r="6"/><path d="M14 48V28h24v20M38 48V32h18v16"/></svg>
        <span class="stat__num">1 in3</span>
      </div>
      <p class="stat__text">American Indian people<br>ages 65+<br>develop dementia</p>
    </div>
  </div>

  <div class="abs keep">
    <h2 class="heading">Keep your heart and body<br>healthy to protect your brain</h2>
    <p class="body-copy">Everyone slows down as they get older, both in body and mind. Big changes in memory or thinking that make it hard to get through the day are not a normal part of aging. These changes could be signs of early dementia or Alzheimer’s disease.</p>
  </div>

  <div class="abs risk">
    <div class="risk__label">You are more at risk of<br>developing dementia if<br>you have</div>
    <div class="risk__item" style="left:345px">
      <svg viewBox="0 0 48 48" fill="none" stroke="#fff" stroke-width="2"><path d="M24 40C10 30 6 22 10 15a8 8 0 0 1 14-1 8 8 0 0 1 14 1c4 7 0 15-14 25z"/><path d="M8 26h8l3-6 4 10 3-6h6"/></svg>
      <span>high blood<br>pressure</span>
    </div>
    <div class="risk__item" style="left:493px">
      <svg viewBox="0 0 48 48" fill="none" stroke="#fff" stroke-width="2"><rect x="12" y="8" width="22" height="26" rx="3"/><rect x="16" y="12" width="14" height="9"/><path d="M23 34v8"/><circle cx="23" cy="27" r="2"/></svg>
      <span>diabetes<br>or</span>
    </div>
    <div class="risk__item" style="left:630px">
      <svg viewBox="0 0 48 48" fill="none" stroke="#fff" stroke-width="2"><path d="M6 42V24l10 6v-6l10 6v-6l10 6V42z"/><path d="M36 30V14h6v28"/><path d="M38 10c2-3 6-3 6-7"/></svg>
      <span>you smoke<br>cigarettes</span>
    </div>
  </div>

  <h2 class="abs heading protect-heading">You can protect your body, heart, and mind</h2>

  <div class="col" style="left:38px;top:868px">
    <ul class="tick-list">
      <li><svg style="color:#777"><use href="#tick"/></svg><span><span class="accent">Schedule a</span> “wellness” visit and health screenings every year with your doctor, even if you feel ok</span></li>
      <li><svg style="color:#777"><use href="#tick"/></svg><span class="accent">Keep a healthy blood pressure</span></li>
      <li><svg style="color:#777"><use href="#tick"/></svg><span><span class="accent">If it is hard for you to get through the day</span> because of forgetfulness or memory problems, see your doctor right away</span></li>
      <li style="width:400px"><svg style="color:#777"><use href="#tick"/></svg><span class="accent">You can do these things today to protect your mind and reduce the risk of or slow down dementia</span></li>
    </ul>
  </div>
  <div class="col" style="left:309px;top:868px">
    <ul class="tick-list">
      <li><svg style="color:#777"><use href="#tick"/></svg><span><span class="accent">Eat a healthier diet</span> with more fresh vegetables, fruits, whole grains, and fish</span></li>
      <li><svg style="color:#777"><use href="#tick"/></svg><span><span class="accent">Be active or walk</span> every day</span></li>
      <li><svg style="color:#777"><use href="#tick"/></svg><span><span class="accent">Talk to your doctor about how you feel</span> because your mental health can affect your brain and physical health</span></li>
    </ul>
  </div>
  <div class="col" style="left:578px;top:868px;width:210px">
    <ul class="tick-list">
      <li><svg style="color:#777"><use href="#tick"/></svg><span><span class="accent">Get help managing</span> your high blood pressure, diabetes, or to lose extra weight</span></li>
      <li><svg style="color:#777"><use href="#tick"/></svg><span><span class="accent">Maintain a healthy weight</span> for your body size</span></li>
      <li><svg style="color:#777"><use href="#tick"/></svg><span><span class="accent">Stop smoking</span> cigarettes or chewing tobacco</span></li>
    </ul>
  </div>

  <footer class="abs footer">
    <div class="footer__phone"><svg width="28" height="28"><use href="#phone"/></svg>(505) 555-0148</div>
    <div class="footer__addr"><svg width="24" height="28"><use href="#pin"/></svg><span>1780 Cedar Mesa Rd NE<br>Riverbend, NM 87000</span></div>
    <div class="footer__web"><svg width="24" height="24"><use href="#globe"/></svg>www.novelmarrow.org</div>
  </footer>
</section>

<!-- BACK PAGE -->
<section class="page page--back">
  <div class="abs river"></div>
  <svg class="abs" style="left:0;top:0" width="814" height="360" viewBox="0 0 814 360" aria-hidden="true">
    <path d="M0 285 C200 325 520 325 814 275 V360 H0 Z" fill="#ffffff"/>
    <path d="M0 285 C200 325 520 325 814 275" fill="none" stroke="#3c9fa9" stroke-width="6"/>
  </svg>

  <div class="abs river__copy">
    <p class="heading river__kicker">The river of life flows through</p>
    <h2 class="heading river__title">Your heart to protect<br>your mind and body</h2>
    <p class="body-copy">Your heart health plays a big part in the health of your brain. Your heart is like the start of a flowing river. Blood vessels that take blood to and from your heart are like connected streams that flow through your body. They feed your brain with oxygen and energy.<br>You can do things to keep the streams freely flowing through your body, so your heart and brain stay strong and healthy.</p>
  </div>

  <div class="abs panel">
    <ul class="tick-list">
      <li><svg style="color:#f1c9c5"><use href="#tick"/></svg><strong>Have your blood pressure checked and know your numbers</strong></li>
      <li><svg style="color:#f1c9c5"><use href="#tick"/></svg><span>Your blood pressure should be less than 120/80 mmHg (120 over 80)</span></li>
      <li><svg style="color:#f1c9c5"><use href="#tick"/></svg><span>If you do not know how to take your blood pressure, ask your doctor to show you</span></li>
      <li><svg style="color:#f1c9c5"><use href="#tick"/></svg><span>If you smoke cigarettes or chew tobacco, ask about medicine, counseling, or help to stop</span></li>
      <li><svg style="color:#f1c9c5"><use href="#tick"/></svg><span>If you do not have diabetes, have your blood sugar level checked during your visit. Your blood sugar should be less than 100mg/dL when you have not eaten.</span></li>
      <li><svg style="color:#f1c9c5"><use href="#tick"/></svg><span>If you do have diabetes, go to regular doctor visits. Have your blood sugar and “A1C” levels checked. Your doctor will tell you what your A1C level should be.</span></li>
      <li><svg style="color:#f1c9c5"><use href="#tick"/></svg><span>Support for losing weight</span></li>
    </ul>
  </div>

  <h2 class="abs heading doctor-heading">Working with your doctor</h2>
  <div class="abs doctor">
    <ul class="tick-list">
      <li><svg style="color:var(--teal)"><use href="#tick"/></svg><span class="accent">Make an appointment for a “wellness” checkup with your doctor every year</span></li>
      <li><svg style="color:var(--teal)"><use href="#tick"/></svg><span>You will get tests and screenings to make sure you are healthy</span></li>
      <li><svg style="color:var(--teal)"><use href="#tick"/></svg><span>They are usually free with Elder Care Plan B or the Tribal Wellness Service</span></li>
      <li><svg style="color:var(--teal)"><use href="#tick"/></svg><span>If you have concerns about your memory, talk to your doctor</span></li>
      <li><svg style="color:var(--teal)"><use href="#tick"/></svg><span>Talk with your doctor about all the medicines and vitamins you take. Your doctor can make sure they do not cause any problems with your memory, sleep, or brain function.</span></li>
      <li><svg style="color:var(--teal)"><use href="#tick"/></svg><span class="accent">Have your weight checked regularly and know your number. If you need to lose extra weight, ask your doctor about</span></li>
      <li><svg style="color:var(--teal)"><use href="#tick"/></svg><span>The right number of calories for your body</span></li>
      <li><svg style="color:var(--teal)"><use href="#tick"/></svg><span>Ideas for healthier food choices</span></li>
    </ul>
  </div>

  <h2 class="abs heading steps-heading">Other steps you can take</h2>
  <div class="col" style="left:38px;top:875px;width:230px">
    <ul class="tick-list">
      <li><svg style="color:var(--teal)"><use href="#tick"/></svg><span>Aim for 20 minutes of physical activity a day or 2 1/2 hours a week</span></li>
      <li><svg style="color:var(--teal)"><use href="#tick"/></svg><span>Eat less salt, sugar, red meat, and highly processed or packaged foods</span></li>
      <li style="width:470px"><svg style="color:var(--teal)"><use href="#tick"/></svg><span><strong>Keep your mind active.</strong> Visit with people in your community, help plan tribal events, go to your senior center, teach your language, play cards, or start a new hobby.</span></li>
    </ul>
  </div>
  <div class="col" style="left:293px;top:875px;width:230px">
    <ul class="tick-list">
      <li><svg style="color:var(--teal)"><use href="#tick"/></svg><span>Read food labels to see how much salt (sodium) or fat is in your food</span></li>
      <li><svg style="color:var(--teal)"><use href="#tick"/></svg><span>Manage extra weight by making small changes. Losing a few pounds makes a difference</span></li>
    </ul>
  </div>
  <div class="col" style="left:551px;top:875px;width:230px">
    <ul class="tick-list">
      <li><svg style="color:var(--teal)"><use href="#tick"/></svg><span>Get at least seven hours of sleep each night. Talk to your doctor if you have trouble sleeping</span></li>
      <li><svg style="color:var(--teal)"><use href="#tick"/></svg><span>Take your medicine for blood pressure, diabetes, and other problems even if you feel good</span></li>
      <li><svg style="color:var(--teal)"><use href="#tick"/></svg><span>Limit alcohol. No more than 1 drink per day for women and 2 for men</span></li>
    </ul>
  </div>

  <footer class="abs footer">
    <div class="footer__phone"><svg width="28" height="28"><use href="#phone"/></svg>(505) 555-0148</div>
    <div class="footer__addr"><svg width="24" height="28"><use href="#pin"/></svg><span>1780 Cedar Mesa Rd NE<br>Riverbend, NM 87000</span></div>
    <div class="footer__web"><svg width="24" height="24"><use href="#globe"/></svg>www.novelmarrow.org</div>
  </footer>
</section>

</body>
</html>
```